Potential SF Gazette Best Seller Poetry Book Cover Contest

I’m penning my first poetry book. It’s entitled “Lanterns Under Rain”
I’m fairly open to creative freedom but I want the cover to without a doubt catch a persons' eye instantly because first impressions are VERY IMPORTANT in the literary world
I tend to lean towards a luxury look and colors like black, gold, rose gold, silver, glitter etc but again I’m open to interpretation
Looking forward to your submissions
Target Market(s)
those seeking relatable love advice and quotes
modern millenials
Colors
Look and feel

```html
<!DOCTYPE html>
<html lang="en">
<head>
<meta charset="utf-8">
<title>Lanterns Under Rain — Cover</title>
<link rel="stylesheet" href="https://fonts.googleapis.com/css2?family=Montserrat:wght@100;200;800&display=swap">
<style>
  :root {
    --paper: #ffffff;
    --ink: #111111;
    --accent-red: #ed1c24;
    --frame-line: #222222;
  }

  html, body {
    margin: 0;
    padding: 0;
    width: 1200px;
    height: 1200px;
    overflow: hidden;
    background: var(--paper);
  }

  .canvas {
    position: relative;
    width: 1200px;
    height: 1200px;
    background: var(--paper);
  }

  .book-cover {
    position: absolute;
    left: 293px;
    top: 139px;
    width: 595px;
    height: 877px;
    box-sizing: border-box;
    border: 1px solid var(--frame-line);
    background: var(--paper);
    display: flex;
    align-items: center;
    justify-content: center;
  }

  .title {
    margin: 0;
    display: flex;
    flex-direction: column;
    align-items: center;
    font-family: "Montserrat", sans-serif;
    color: var(--ink);
    text-align: center;
    transform: translateY(-8px);
  }

  .title__line {
    display: block;
    line-height: 1;
  }

  .title__line--light {
    font-weight: 100;
    font-size: 96px;
    letter-spacing: -1px;
    line-height: 92px;
  }

  .title__line--bold {
    font-weight: 800;
    font-size: 132px;
    letter-spacing: -4px;
    line-height: 118px;
    color: var(--accent-red);
    margin: 2px 0 4px;
  }

  .title__accent-letter {
    color: var(--ink);
  }
</style>
</head>
<body>
  <main class="canvas">
    <section class="book-cover" aria-label="Poetry book cover">
      <h1 class="title">
        <span class="title__line title__line--light">lanterns</span>
        <span class="title__line title__line--bold">un<span class="title__accent-letter">d</span>er</span>
        <span class="title__line title__line--light">rain.</span>
      </h1>
    </section>
  </main>
</body>
</html>
```